Webdesign for a Bikeshop in Innsbruck (male audience)

To obtain my master's degree, I am conducting a study in the field of web design as part of my master thesis. All submitted designs will therefore be used for study purposes. In order to achieve a homogeneous group, I would like to encourage not only male but also female web designers to submit a design. All submitted designs will be used anonymously for the study and therefore do not allow any conclusions to be drawn about your person. Since this is a contest, the winner will be chosen randomly from all serious submissions. I would be really happy if you would support me in my study. I think the results could be very informative and also useful for your further work (I won't go into more detail here as it could skew the results - but once the contest is over, feel free to contact me. Of course I will also provide you with my results as soon as my work is finished). Below you will find a fictitious usecase and a description of what the website should include:

The company Veloria Kastwerk is planning to relaunch its own website and would like to present itself primarily as a competent and leading consultant in the field of cargo bikes. The design should appeal to a broad audience and embody an urban lifestyle. In any case, the website should include a landing page, a product overview page and a product details page. The company also wants to appeal mainly to a MALE target group. You only design the website. So don't worry about hardware or software limitations, just create the best bike store design you can.

As it is fictitious, I can't offer any materials. A logo is not necessary, you can use a placeholder or whatever you have access to. If you need any inspring websites feel free to contact me.

Target Market(s)

male users

Number of Pages Required

1 page

Requirements
Must have
• landing page, product overview page, product details page
Should not have
• online shop

```html
<!DOCTYPE html>
<html lang="en">
<head>
<meta charset="utf-8">
<title>Veloria Kastwerk – Cargo Bikes</title>
<link href="https://fonts.googleapis.com/css2?family=Oswald:wght@400;500;700&family=Open+Sans:wght@400;600&display=swap" rel="stylesheet">
<style>
:root{
  --sand:#ddd7bc;
  --sand-deep:#cfc7a2;
  --sand-light:#e9e5d3;
  --grey-light:#ececea;
  --grey-band:#e2e2e0;
  --ink:#2b2b2b;
  --ink-soft:#6b6b63;
  --white:#ffffff;
  --ghost:rgba(160,150,110,.35);
  --accent:#3a3a36;
}
*{box-sizing:border-box;margin:0;padding:0}
html,body{width:694px;height:1200px;overflow:hidden}
body{background:var(--white);font-family:'Open Sans',sans-serif;color:var(--ink);position:relative}
.page{position:relative;width:694px;height:1200px;overflow:hidden}
.heading{font-family:'Oswald',sans-serif}

/* header & hero */
.hero{position:absolute;top:0;left:0;width:694px;height:302px;background:linear-gradient(180deg,#e3ddc4 0%,#d6cfb0 100%);overflow:hidden}
.site-header{position:absolute;top:0;left:0;width:100%;height:36px;display:flex;align-items:center;justify-content:space-between;padding:0 18px}
.brand-mark{font-family:'Oswald',sans-serif;font-weight:700;font-size:20px;color:var(--ink)}
.main-nav{display:flex;gap:22px}
.main-nav a{font-family:'Oswald',sans-serif;font-size:12px;font-weight:500;color:var(--ink);text-decoration:none;letter-spacing:.5px}
.hero-ghost{position:absolute;left:132px;top:36px;font-family:'Oswald',sans-serif;font-weight:700;font-size:92px;line-height:.88;color:var(--ghost)}
.hero-bike{position:absolute;left:210px;top:92px;width:280px;height:150px;border-radius:14px;background:radial-gradient(ellipse at 60% 45%,#f4f4f2 0%,#bdbdb8 45%,rgba(60,60,60,.5) 75%,rgba(0,0,0,0) 100%)}
.hero-tagline{position:absolute;top:262px;width:100%;text-align:center;font-family:'Oswald',sans-serif;font-weight:500;font-size:17px;color:var(--white);letter-spacing:.6px}

/* categories */
.categories{position:absolute;top:318px;left:0;width:694px;height:92px;display:flex;gap:4px;padding:0 2px}
.category{position:relative;flex:1;overflow:hidden}
.category-photo{position:absolute;inset:0;background:linear-gradient(135deg,#b9b4a2,#8e8a7c 60%,#a7a290)}
.category-label{position:absolute;left:22px;top:38px;font-family:'Oswald',sans-serif;font-weight:500;font-size:18px;line-height:1;color:var(--white)}

/* best sellers */
.best-sellers{position:absolute;top:412px;left:0;width:694px;height:184px;background:var(--grey-light)}
.section-title{font-family:'Oswald',sans-serif;font-weight:400;font-size:17px;text-align:center;color:var(--ink)}
.best-sellers .section-title{margin-top:10px}
.product-row{display:flex;justify-content:center;gap:26px;margin-top:12px}
.product{width:160px;text-align:center}
.product-photo{height:92px;border-radius:8px}
.photo-teal{background:radial-gradient(ellipse at 50% 55%,#6cc4c1 0%,#9fb7b3 40%,rgba(236,236,234,0) 72%)}
.photo-wood{background:radial-gradient(ellipse at 50% 55%,#d68a3c 0%,#b89a78 40%,rgba(236,236,234,0) 72%)}
.photo-lime{background:radial-gradient(ellipse at 50% 55%,#c5db3a 0%,#b8c07a 40%,rgba(236,236,234,0) 72%)}
.product-type{font-size:6px;color:var(--ink-soft);margin-top:6px;letter-spacing:.3px}
.product-name{font-family:'Oswald',sans-serif;font-size:12px;font-weight:500;margin-top:1px}

/* feature blocks */
.feature{position:absolute;left:0;width:694px;overflow:hidden}
.feature-learn{top:604px;height:160px;background:var(--sand)}
.feature-advantage{top:780px;height:160px;background:var(--sand-light)}
.feature-ghost{position:absolute;font-family:'Oswald',sans-serif;font-weight:700;font-size:46px;line-height:.9;color:var(--ghost)}
.feature-photo{position:absolute;width:270px;height:110px;border-radius:10px}
.photo-dark{background:radial-gradient(ellipse at 50% 55%,#2f3a4a 0%,#5b6068 40%,rgba(221,215,188,0) 72%)}
.photo-black{background:radial-gradient(ellipse at 50% 55%,#2a2a2a 0%,#6a6a66 40%,rgba(233,229,211,0) 72%)}
.feature-text{position:absolute;width:270px}
.feature-text h2{font-family:'Oswald',sans-serif;font-weight:500;font-size:21px;line-height:1.15;color:var(--ink)}
.feature-text p{font-size:11px;line-height:1.45;color:var(--ink-soft);margin-top:6px}
.read-more{display:inline-block;margin-top:8px;font-family:'Oswald',sans-serif;font-size:9px;color:var(--ink);text-decoration:underline}

/* brands */
.brands{position:absolute;top:950px;left:0;width:694px;height:92px;background:var(--grey-band)}
.brands .section-title{margin-top:12px}
.brand-row{display:flex;justify-content:center;align-items:center;gap:22px;margin-top:16px}
.brand-name{font-family:'Oswald',sans-serif;font-weight:500;font-size:17px;color:#9a9a96}

/* footer */
.site-footer{position:absolute;top:1048px;left:0;width:694px;height:152px;background:var(--sand-deep);padding:20px 22px}
.footer-brand{position:absolute;left:74px;top:20px;font-family:'Oswald',sans-serif;font-weight:700;font-size:22px;line-height:1;color:var(--white)}
.footer-contact{position:absolute;left:74px;top:76px;font-size:6px;line-height:1.6;color:var(--ink)}
.footer-col{position:absolute;top:22px}
.footer-col h3{font-family:'Oswald',sans-serif;font-size:8px;font-weight:500;color:var(--ink);margin-bottom:5px}
.footer-col li{list-style:none;font-size:6px;line-height:1.55;color:var(--ink)}
.newsletter{position:absolute;left:456px;top:22px;width:170px}
.newsletter h3{font-family:'Oswald',sans-serif;font-size:8px;font-weight:500}
.newsletter p{font-size:6px;line-height:1.4;margin-top:3px}
.newsletter-form{display:flex;margin-top:8px}
.newsletter-input{width:110px;height:14px;background:var(--white);font-size:6px;color:#999;padding:3px 5px}
.newsletter-btn{height:14px;padding:3px 8px;background:var(--accent);color:var(--white);font-size:6px}
.social{display:flex;gap:4px;margin-top:8px}
.social span{width:10px;height:10px;background:var(--accent);display:block}
.copyright{position:absolute;bottom:10px;width:100%;left:0;text-align:center;font-size:5px;color:var(--ink)}
</style>
</head>
<body>
<div class="page">

  <section class="hero">
    <header class="site-header">
      <div class="brand-mark">VK</div>
      <nav class="main-nav"><a href="#">CATALOG</a><a href="#">ABOUT US</a><a href="#">CONTACT</a></nav>
    </header>
    <div class="hero-ghost" aria-hidden="true">Veloria<br>Kastwerk</div>
    <div class="hero-bike" role="img" aria-label="White electric cargo bike with a large front box"></div>
    <p class="hero-tagline">YOUR LEADING CONSULTANT OF CARGO BIKES</p>
  </section>

  <section class="categories">
    <a class="category"><div class="category-photo" role="img" aria-label="Father riding a family cargo bike with children"></div><span class="category-label">FAMILY<br>CARGO BIKES</span></a>
    <a class="category"><div class="category-photo" role="img" aria-label="Courier delivering parcels on a cargo bike"></div><span class="category-label">DELIVERY<br>CARGO BIKES</span></a>
    <a class="category"><div class="category-photo" role="img" aria-label="Cargo bike accessories on a city street"></div><span class="category-label">ACCESSORIES</span></a>
  </section>

  <section class="best-sellers">
    <h2 class="section-title">BEST SELLERS</h2>
    <div class="product-row">
      <div class="product"><div class="product-photo photo-teal" role="img" aria-label="Teal longtail cargo bike"></div><div class="product-type">ELECTRIC</div><div class="product-name">KORVO TRAIL RUNNER</div></div>
      <div class="product"><div class="product-photo photo-wood" role="img" aria-label="Black cargo bike with wooden front box"></div><div class="product-type">ELECTRIC &amp; NON-ELECTRIC</div><div class="product-name">LASTRA METRO</div></div>
      <div class="product"><div class="product-photo photo-lime" role="img" aria-label="Lime green longtail electric cargo bike"></div><div class="product-type">ELECTRIC</div><div class="product-name">KORVO HOT PEPPER</div></div>
    </div>
  </section>

  <section class="feature feature-learn">
    <div class="feature-ghost" style="left:90px;top:20px" aria-hidden="true">Veloria<br>Kastwerk</div>
    <div class="feature-photo photo-dark" style="left:70px;top:24px" role="img" aria-label="Dark blue cargo bike with covered front box"></div>
    <div class="feature-text" style="left:356px;top:40px">
      <h2>Learn which cargo bike is best for you.</h2>
      <p>Lorem ipsum dolor sit amet, consectetuer adipiscing elit, sed diam nonummy nibh euismod.</p>
      <a class="read-more" href="#">READ MORE</a>
    </div>
  </section>

  <section class="feature feature-advantage">
    <div class="feature-ghost" style="left:390px;top:22px" aria-hidden="true">Veloria<br>Kastwerk</div>
    <div class="feature-text" style="left:86px;top:30px">
      <h2>The advantage of using cargo bikes.</h2>
      <p>Lorem ipsum dolor sit amet, consectetuer adipiscing elit, sed diam nonummy nibh euismod.</p>
      <a class="read-more" href="#">READ MORE</a>
    </div>
    <div class="feature-photo photo-black" style="left:350px;top:30px" role="img" aria-label="Black electric cargo bike with flat front platform"></div>
  </section>

  <section class="brands">
    <h2 class="section-title">OUR BEST BRANDS</h2>
    <div class="brand-row">
      <span class="brand-name">STADTLINE</span>
      <span class="brand-name">LASTRA</span>
      <span class="brand-name">pakko</span>
      <span class="brand-name">frachta</span>
      <span class="brand-name">rollund</span>
      <span class="brand-name">velo9</span>
      <span class="brand-name">alpbike</span>
      <span class="brand-name">korvo</span>
    </div>
  </section>

  <footer class="site-footer">
    <div class="footer-brand">Veloria<br>Kastwerk</div>
    <div class="footer-contact">hello@veloria-kastwerk.at<br>+43 512 000 000</div>
    <div class="footer-col" style="left:250px"><h3>SUPPORT</h3><ul><li>FAQ</li><li>Warranty</li><li>Assembly</li></ul></div>
    <div class="footer-col" style="left:308px"><h3>MENU</h3><ul><li>Catalog</li><li>About Us</li><li>Contact</li></ul></div>
    <div class="footer-col" style="left:360px"><h3>LEGAL INFO</h3><ul><li>Terms &amp; Conditions</li><li>Privacy Policy</li><li>Repair Policy</li></ul></div>
    <div class="newsletter">
      <h3>SUBSCRIBE TO OUR NEWSLETTER</h3>
      <p>Get our best tips about cargo bikes, offers and news.</p>
      <div class="newsletter-form"><div class="newsletter-input">E-mail</div><div class="newsletter-btn">Sign Up</div></div>
      <div class="social"><span></span><span></span><span></span><span></span><span></span></div>
    </div>
    <p class="copyright">© 2024 Veloria Kastwerk. All rights reserved.</p>
  </footer>

</div>
</body>
</html>
```